Seriöses Webdesign für innovatives Ingenieurbüro mit dem Schwerpunkt Eisenbahn Leit- und Sicherungstechnik
Zielgruppe
Die Webseite hat in erster Linie die Aufgabe zu informieren: An erster Stelle steht die Kontaktaufnahme und der Kompetenzbereich des Ingenieurbüros.
Folgende Kernkompetenzen sollen durch die Webseite transportiert werden:
Hardware-Entwicklung
Software-Entwicklung
Erneuerung alter Techniken
Begutachtung
Software für Lieferantenbewertung
Störungsmanagement(system)
Zielgruppe:
Die Webseite soll als Online-Visitenkarte für bestehende und neue Kontakte dienen. Gerade neue (Messe-)Kontakte erleben die Webseite als erste Anlaufstelle und erhalten einen Einblick in das vorhandene Leistungsspektrum des Ingenieurbüros und die Möglichkeiten der Kontaktaufnahme.

```html
<!DOCTYPE html>
<html lang="de">
<head>
<meta charset="utf-8">
<title>Nordgleis – Ingenieurbüro für Verkehrstechnik</title>
<link href="https://fonts.googleapis.com/css2?family=Source+Sans+3:wght@400;600;700&display=swap" rel="stylesheet">
<style>
  :root {
    --sky: #7cc3e2;
    --sky-light: #dceefa;
    --slate: #2c3842;
    --slate-soft: #3a4751;
    --ink: #2a2f33;
    --paper: #ffffff;
    --stone: #e3e3e3;
    --rule: #3a444c;
  }
  * { margin: 0; padding: 0; box-sizing: border-box; }
  html, body { width: 922px; height: 1200px; overflow: hidden; }
  body {
    position: relative;
    font-family: "Source Sans 3", "Source Sans Pro", sans-serif;
    color: var(--ink);
    background: var(--paper);
  }
  .abs { position: absolute; }

  /* Header */
  .site-header { left: 0; top: 0; width: 922px; height: 76px; background: var(--sky); }
  .brand { left: 138px; top: 14px; font-size: 30px; font-weight: 700; color: var(--paper); letter-spacing: 0.5px; line-height: 1; }
  .tagline { left: 138px; top: 48px; font-size: 11px; font-weight: 600; color: var(--slate); }
  .lang { left: 732px; top: 30px; display: flex; align-items: center; font-size: 8px; font-weight: 700; }
  .lang span { padding: 3px 6px; }
  .lang .active { background: var(--paper); color: var(--ink); }
  .lang .other { background: #bfe0ef; color: var(--slate); }

  /* Hero */
  .hero { left: 0; top: 76px; width: 922px; height: 271px;
    background: linear-gradient(180deg, #8e9aa6 0%, #b6bec6 45%, #9fa392 70%, #6f6a5c 100%); }
  .service-menu { left: 138px; top: 117px; width: 216px; height: 144px; background: var(--sky-light);
    border-radius: 6px; padding: 11px 15px 0 15px; list-style: none; }
  .service-menu li { height: 21px; line-height: 21px; font-size: 11px; font-weight: 600; color: var(--slate);
    padding-left: 5px; border-bottom: 1px solid var(--slate); }
  .service-menu li:last-child { border-bottom: none; }
  .service-menu li.current { background: var(--slate); color: var(--paper); }
  .hero-edge { left: 0; top: 347px; width: 922px; height: 3px; background: var(--paper); }

  /* Intro */
  .intro { left: 0; top: 350px; width: 922px; height: 240px; background: var(--slate); }
  .intro-title { left: 136px; top: 377px; font-size: 32px; font-weight: 400; line-height: 35px; color: var(--paper); }
  .intro-sub { left: 136px; top: 454px; font-size: 14.5px; font-weight: 600; color: var(--sky); }
  .intro-text { left: 137px; top: 499px; width: 312px; font-size: 10.5px; line-height: 17px; color: var(--paper); }
  .intro-visual { left: 305px; top: 368px; width: 222px; height: 75px; background: var(--slate-soft); border-radius: 3px; }
  .contact-btn { left: 601px; top: 437px; width: 125px; height: 31px; background: var(--sky); border-radius: 2px;
    font-size: 17px; font-weight: 700; color: var(--slate); padding-left: 14px; line-height: 31px; }
  .contact-phone { left: 615px; top: 480px; font-size: 10.5px; font-weight: 700; color: var(--paper); }
  .contact-mail { left: 615px; top: 500px; font-size: 10.5px; font-weight: 700; color: var(--sky); }

  /* Feature */
  .feature-title { left: 138px; top: 618px; font-size: 25px; font-weight: 600; color: var(--slate); letter-spacing: 0.3px; }
  .col { width: 184px; font-size: 11px; line-height: 15.5px; color: var(--ink); }
  .col p + p { margin-top: 15.5px; }
  .feature-image { left: 608px; top: 616px; width: 117px; height: 224px; border-radius: 3px;
    background: linear-gradient(180deg, #d4d6d8 0%, #b8bbbe 40%, #6d7a80 70%, #9aa1a5 100%);
    border: 3px solid #e6e6e6; }
  .divider { left: 0; top: 868px; width: 922px; height: 3px; background: var(--rule); }

  /* Info band */
  .info-band { left: 0; top: 874px; width: 922px; height: 225px; background: var(--stone); }

  /* Footer */
  .site-footer { left: 0; top: 1102px; width: 922px; height: 98px; background: var(--sky); }
  .footer-brand { left: 137px; top: 1128px; font-size: 30px; font-weight: 700; color: var(--paper); letter-spacing: 0.5px; line-height: 1; }
  .footer-links { left: 137px; top: 1173px; font-size: 9.5px; font-weight: 600; color: var(--slate); }
  .footer-btn { top: 1138px; width: 129px; height: 24px; border: 1px solid var(--paper); border-radius: 3px;
    font-size: 10.5px; font-weight: 700; color: var(--paper); text-align: center; line-height: 22px; }
</style>
</head>
<body>
  <header class="abs site-header"></header>
  <div class="abs brand">Nordgleis</div>
  <div class="abs tagline">Ingenieurbüro für Verkehrstechnik</div>
  <div class="abs lang"><span class="active">DE</span><span class="other">ENG</span></div>

  <div class="abs hero" role="img" aria-label="Foto: zwei Hochgeschwindigkeitszüge vor einer Wartungshalle auf Gleisen"></div>
  <ul class="abs service-menu">
    <li>Software</li>
    <li>Hardware</li>
    <li class="current">Begutachtung</li>
    <li>Erneuerung alter Techniken</li>
    <li>Software für Lieferantenbewertung</li>
    <li>Störungsmanagement</li>
  </ul>
  <div class="abs hero-edge"></div>

  <section class="abs intro"></section>
  <h1 class="abs intro-title">Wir stellen<br>Weichen</h1>
  <div class="abs intro-visual" role="img" aria-label="Illustration: Monitor, gestrichelte Linie und Weichensymbol"></div>
  <div class="abs intro-sub">Maßgeschneiderte Softwarelösungen</div>
  <p class="abs intro-text">Hier sollte ein Text stehen, der uns zum Vorteil gereift. Hier sollte ein Text stehen, der uns zum Vorteil gereift. Hier sollte ein Text stehen, der uns zum Vorteil</p>
  <div class="abs contact-btn">&gt;&gt; Kontakt</div>
  <div class="abs contact-phone">T 0 800 - 12 34 56 78</div>
  <div class="abs contact-mail">info@nordgleis.de</div>

  <h2 class="abs feature-title">Erneuerung der alten Technik</h2>
  <div class="abs col" style="left:138px; top:670px;">
    <p>Hier sollte ein Text stehen, der uns zum Vorteil gereift. Hier sollte ein Text stehen.</p>
    <p>Hier sollte ein Text stehen, der uns zum Vorteil gereift. Hier sollte ein Text stehen. Hier sollte ein Text stehen, der uns zum Vorteil gereift. Hier sollte ein Text stehen.</p>
  </div>
  <div class="abs col" style="left:364px; top:670px;">
    <p>Hier sollte ein Text stehen, der uns zum Vorteil gereift. Hier sollte ein Text stehen.</p>
    <p>Hier sollte ein Text stehen, der uns zum Vorteil gereift. Hier sollte ein Text stehen. Hier sollte ein Text stehen, der uns zum Vorteil gereift. Hier sollte ein Text stehen.</p>
  </div>
  <div class="abs feature-image" role="img" aria-label="Foto: geöffneter Schaltschrank mit Steuerungsbaugruppen"></div>
  <div class="abs divider"></div>

  <section class="abs info-band" role="img" aria-label="Dezentes Hintergrundmuster aus Gleisplan-Symbolen"></section>
  <div class="abs col" style="left:138px; top:913px;">
    <p>Hier sollte ein Text stehen, der uns zum Vorteil gereift. Hier sollte ein Text stehen.</p>
    <p>Hier sollte ein Text stehen, der uns zum Vorteil gereift. Hier sollte ein Text stehen. Hier sollte ein Text stehen, der uns zum Vorteil gereift. Hier sollte ein Text stehen.</p>
  </div>
  <div class="abs col" style="left:364px; top:913px;">
    <p>Hier sollte ein Text stehen, der uns zum Vorteil gereift. Hier sollte ein Text stehen.</p>
    <p>Hier sollte ein Text stehen, der uns zum Vorteil gereift. Hier sollte ein Text stehen. Hier sollte ein Text stehen, der uns zum Vorteil gereift. Hier sollte ein Text stehen.</p>
  </div>
  <div class="abs col" style="left:597px; top:913px;">
    <p>Hier sollte ein Text stehen, der uns zum Vorteil gereift. Hier sollte ein Text stehen.</p>
    <p>Hier sollte ein Text stehen, der uns zum Vorteil gereift. Hier sollte ein Text stehen. Hier sollte ein Text stehen, der uns zum Vorteil gereift. Hier sollte ein Text stehen.</p>
  </div>

  <footer class="abs site-footer"></footer>
  <div class="abs footer-brand">Nordgleis</div>
  <nav class="abs footer-links">Startseite &nbsp;•&nbsp; AGB &nbsp;•&nbsp; Bankverbindung &nbsp;•&nbsp; Datenschutz &nbsp;•&nbsp; Impressum</nav>
  <div class="abs footer-btn" style="left:527px;">Downloads &gt;&gt;</div>
  <div class="abs footer-btn" style="left:666px;">Nachricht senden &gt;&gt;</div>
</body>
</html>
```